Business card design needed to incorporate existing logo

We need a business card for a new modern Accounting & Business Solutions company call Kelvra Partners.com.au servicing all of Australia.
My tagline is Steady Ledger Answers... done right.

We specialise in Cloud Accounting and this is our primary focus. We also provide tax representation, debt recovery, computer, tablet and smart phone sales.

I would like a design that uses my corporate, trustworthy colours of blue/white, black/grey however am open to suggestion. I have attached my logo to go on the card somewhere,of which you will see the colour scheme.

I am after a card that STANDS OUT, somewhere between it not being too busy and not being a baron waste of space.

A 'cloud' incorporated in the design may work well, up to your artistic judgement. I know what I like when I see it; it is harder to put into words!

Excited to see your ideas!
I have added my logo predominately (blue/white) and for additional opportunity have added my reverse logo (darker one). I have used the blue/white on my website and letterhead. I will be using both on my vehicle signage.

Target Market(s)

Tradesmen and small-medium businesses of all descriptions Australia-wide

Industry/Entity Type

Debt

Contact Information for Business Card

Dale Fenwick
Principal (optional)
Kelvra Partners.com.au
Steady Ledger Answers... done right

P: 1800 530 918
M: 0418 652 074 (optional)
W: www.kelvrapartners.example
E: admin@kelvrapartners.example

Logo Text

Steady Ledger Answers... done right!

Logo styles of interest
Wordmark Logo
Requirements
Must have
• Must look professional and of high quality not cheap.

My logo and my tagline 'Steady Ledger Answers... done right'.

I have my colourscheme in mind as per my attached logo, however am open to suggestion. I want to see what you can create that I would not have thought of.

Modern, innovative.
Something I won't look at and think, 'I could have done that myself'.

Must be able to be printed on Plimo 300gm premium cards and the artwork provided to me.
Nice to have
• Title of Principal is optional depending on space and judement call of look/fee.
M: (mobile) number is also optional as above.

Somthing cloud related given the Cloud Accounting aspect may be relevant. I leave it to your artistic design and judgement.
Should not have
• Must not look cheap.

```html
<!DOCTYPE html>
<html lang="en">
<head>
<meta charset="utf-8">
<title>Kelvra Partners – Business Card</title>
<link rel="stylesheet" href="https://fonts.googleapis.com/css2?family=Open+Sans:wght@300;400;700;800&display=swap">
<style>
  :root {
    --stage: #262626;
    --navy: #1f2a5c;
    --navy-deep: #1a2350;
    --sky: #2f8fd6;
    --sky-light: #59b4ec;
    --white: #ffffff;
    --ink: #1f2a5c;
  }
  * { box-sizing: border-box; margin: 0; padding: 0; }
  html, body {
    width: 1200px; height: 1200px; overflow: hidden;
    background: var(--stage);
    font-family: "Open Sans", Arial, sans-serif;
  }
  .canvas { position: relative; width: 1200px; height: 1200px; }

  .card {
    position: absolute; left: 150px; width: 900px; height: 514px;
    overflow: hidden;
    box-shadow: 0 18px 40px rgba(0,0,0,.55);
  }
  .card--front { top: 60px; background: var(--navy); }
  .card--back { top: 626px; background: var(--white); }

  /* front */
  .tab {
    position: absolute; background: var(--white); border-radius: 22px;
  }
  .tab--upper { right: -30px; top: 38px; width: 200px; height: 178px; }
  .tab--lower { left: -30px; top: 270px; width: 200px; height: 178px; }

  .front-logo {
    position: absolute; left: 0; right: 0; top: 188px; text-align: center;
  }
  .wordmark {
    font-weight: 300; color: var(--sky-light); letter-spacing: .06em;
    white-space: nowrap;
  }
  .front-logo .wordmark { font-size: 58px; }

  .web-line {
    position: absolute; right: 70px; top: 432px;
    color: var(--white); font-size: 24px; font-weight: 400; letter-spacing: .08em;
  }
  .stripe-rule {
    position: absolute; left: 0; right: 0; top: 470px; height: 4px; background: var(--white);
  }
  .stripe-band {
    position: absolute; left: 0; right: 0; top: 478px; height: 12px; background: var(--sky);
  }

  /* back */
  .back-logo {
    position: absolute; left: 0; width: 460px; top: 218px; text-align: center;
  }
  .back-logo .wordmark { font-size: 40px; color: var(--sky); }

  .divider { position: absolute; top: 0; left: 0; width: 900px; height: 514px; }

  .details {
    position: absolute; left: 530px; top: 70px; color: var(--white);
    font-weight: 700; line-height: 1.25;
  }
  .details .person { font-size: 38px; font-weight: 800; }
  .details .role { font-size: 27px; margin-bottom: 6px; }
  .details .firm, .details .tagline { font-size: 20px; }
  .contact { list-style: none; margin-top: 26px; font-size: 19px; line-height: 1.55; }
</style>
</head>
<body>
<main class="canvas">

  <section class="card card--front" aria-label="Card front">
    <div class="tab tab--upper"></div>
    <div class="tab tab--lower"></div>
    <div class="front-logo"><span class="wordmark">Kelvra Partners</span></div>
    <p class="web-line">www.kelvrapartners.example</p>
    <div class="stripe-rule"></div>
    <div class="stripe-band"></div>
  </section>

  <section class="card card--back" aria-label="Card back">
    <svg class="divider" viewBox="0 0 900 514" aria-hidden="true">
      <rect x="500" y="0" width="400" height="514" fill="#1f2a5c"/>
      <rect x="462" y="0" width="14" height="514" fill="#1f2a5c"/>
      <polygon points="500,150 486,162 500,174" fill="#ffffff"/>
    </svg>
    <div class="back-logo"><span class="wordmark">Kelvra Partners</span></div>
    <div class="details">
      <p class="person">Dale Fenwick</p>
      <p class="role">Principal</p>
      <p class="firm">Kelvra Partners.com.au</p>
      <p class="tagline">Steady Ledger Answers... done right</p>
      <ul class="contact">
        <li>P: 1800 530 918</li>
        <li>M: 0418 652 074</li>
        <li>E: admin@kelvrapartners.example</li>
        <li>W: www.kelvrapartners.example</li>
      </ul>
    </div>
  </section>

</main>
</body>
</html>
```